Letterhead Design Project

Please see attached logo as well as information below which could be relevant to design. Let me know if you have any questions.

Derek J. Vollman
Estate Planning and Insurance Specialist
Dvollman@vollmanadvisory.com
P: 555-298-4153 F: 555-298-4187
www.vollmanadvisory.com
4150 Brindlemoor Parkway, Suite 317E
Calder Point, Westhaven 11804

Insurance

```html
<!DOCTYPE html>
<html lang="en">
<head>
<meta charset="utf-8">
<title>Vollman Advisory Group – Stationery</title>
<link href="https://fonts.googleapis.com/css2?family=Oswald:wght@300;400&family=Open+Sans:wght@400;700&family=Great+Vibes&display=swap" rel="stylesheet">
<style>
  :root{
    --navy:#3c3f51;
    --gold:#c4a96c;
    --ink:#5b5b5b;
    --paper:#ffffff;
    --backdrop:#e8e8eb;
    --light:#e4e5ea;
  }
  *{box-sizing:border-box;margin:0;padding:0}
  html,body{width:1200px;height:706px;overflow:hidden;background:var(--backdrop)}
  .canvas{position:relative;width:1200px;height:706px}

  /* Business cards */
  .card{position:absolute;width:330px;height:188px;background:var(--navy);box-shadow:0 3px 8px rgba(0,0,0,.18)}
  .card-front{left:150px;top:120px;display:flex;align-items:center;justify-content:center}
  .card-front .brand{font-family:"Oswald",sans-serif;font-weight:400;font-size:20px;letter-spacing:3px;color:var(--gold);text-transform:uppercase}
  .card-back{left:150px;top:380px;padding:18px 20px;color:var(--light);font-family:"Oswald",sans-serif;font-weight:300}
  .card-back .brand{font-family:"Oswald",sans-serif;font-weight:400;font-size:15px;letter-spacing:2px;color:var(--gold);text-transform:uppercase}
  .card-back .person{margin-top:14px;font-size:13px;letter-spacing:1px;text-transform:uppercase;color:#fff;font-weight:400}
  .card-back .role{font-size:9px;letter-spacing:.5px}
  .card-back .details{position:absolute;left:20px;right:20px;bottom:16px;display:flex;justify-content:space-between;align-items:flex-end;font-size:8.5px;line-height:1.45}
  .contact-grid{display:grid;grid-template-columns:26px auto;column-gap:4px}
  .contact-grid .label{opacity:.7}

  /* Letterhead */
  .letterhead{position:absolute;left:640px;top:24px;width:470px;height:658px;background:var(--paper);box-shadow:0 4px 12px rgba(0,0,0,.16)}
  .lh-band{position:absolute;left:0;right:0;top:20px;height:54px;background:var(--navy);display:flex;align-items:center;padding:0 18px;color:var(--light);font-family:"Oswald",sans-serif;font-weight:300;font-size:7px;line-height:1.45}
  .lh-brand{flex:1}
  .lh-brand .brand{font-family:"Oswald",sans-serif;font-weight:400;font-size:13px;letter-spacing:1.6px;color:var(--gold);text-transform:uppercase}
  .lh-band .contact-grid{grid-template-columns:20px auto;margin-right:26px}
  .lh-body{position:absolute;left:48px;right:40px;top:110px;font-family:"Open Sans",sans-serif;color:var(--ink);font-size:7.6px;line-height:1.55}
  .lh-body .salutation{font-weight:700;color:#333;margin-bottom:10px}
  .lh-body p{margin-bottom:8px}
  .signature{margin-top:22px}
  .signature .sign{font-family:"Great Vibes",cursive;font-size:24px;color:#333;line-height:1}
  .signature .title{font-weight:700;color:#555;font-size:7.6px}
</style>
</head>
<body>
<div class="canvas">

  <section class="card card-front" aria-label="Business card front">
    <span class="brand">Vollman Advisory Group</span>
  </section>

  <section class="card card-back" aria-label="Business card back">
    <div class="brand">Vollman Advisory Group</div>
    <div class="person">Derek J. Vollman</div>
    <div class="role">Estate Planning and Insurance Specialist</div>
    <div class="details">
      <div class="contact-grid">
        <span class="label">tel</span><span>555-298-4153</span>
        <span class="label">fax</span><span>555-298-4187</span>
        <span class="label">email</span><span>Dvollman@vollmanadvisory.com</span>
      </div>
      <div class="address">4150 Brindlemoor Parkway, Suite 317E<br>Calder Point, Westhaven 11804<br>www.vollmanadvisory.com</div>
    </div>
  </section>

  <article class="letterhead" aria-label="Letterhead">
    <header class="lh-band">
      <div class="lh-brand"><span class="brand">Vollman Advisory Group</span></div>
      <div class="contact-grid">
        <span class="label">tel</span><span>555-298-4153</span>
        <span class="label">fax</span><span>555-298-4187</span>
        <span class="label">email</span><span>Dvollman@vollmanadvisory.com</span>
      </div>
      <div class="address">4150 Brindlemoor Parkway, Suite 317E<br>Calder Point, Westhaven 11804<br>www.vollmanadvisory.com</div>
    </header>
    <div class="lh-body">
      <div class="salutation">Lorem ipsum,</div>
      <p>Cras mattis consectetur purus sit amet fermentum. Etiam porta sem malesuada magna mollis euismod. Integer posuere erat a ante venenatis dapibus posuere velit aliquet. Cras justo odio, dapibus ac facilisis in, egestas eget quam. Aenean eu leo quam. Pellentesque ornare sem lacinia quam venenatis vestibulum.</p>
      <p>Vivamus sagittis lacus vel augue laoreet rutrum faucibus dolor auctor. Donec sed odio dui. Etiam porta sem malesuada magna mollis euismod. Morbi leo risus, porta ac consectetur ac, vestibulum at eros. Nullam id dolor id nibh ultricies vehicula ut id elit.</p>
      <p>Donec id elit non mi porta gravida at eget metus. Fusce dapibus, tellus ac cursus commodo, tortor mauris condimentum nibh, ut fermentum massa justo sit amet risus. Cras justo odio, dapibus ac facilisis in, egestas eget quam. Cum sociis natoque penatibus et magnis dis parturient montes, nascetur ridiculus mus.</p>
      <p>Cum sociis natoque penatibus et magnis dis parturient montes, nascetur ridiculus mus. Curabitur blandit tempus porttitor. Aenean lacinia bibendum nulla sed consectetur. Lorem ipsum dolor sit amet, consectetur adipiscing elit.</p>
      <p>Cras justo odio, dapibus ac facilisis in, egestas eget quam. Morbi leo risus, porta ac consectetur ac, vestibulum at eros. Duis mollis, est non commodo luctus, nisi erat porttitor ligula, eget lacinia odio sem nec elit. Integer posuere erat a ante venenatis dapibus posuere velit aliquet. Vivamus sagittis lacus vel augue laoreet rutrum faucibus dolor auctor.</p>
      <div class="signature">
        <div class="sign">Your Name</div>
        <div class="title">Company Director</div>
      </div>
    </div>
  </article>

</div>
</body>
</html>
```